Business card design and logo needed - Photographer

I take photos of weddings, rodeos, snowmobiling.
Need a card to hand out to prospective clients.
Industry/Entity Type
Business
Contact Information for Business Card
Marcus Dolven Photography
Requirements
Must have
- Bold
Black or white base.
My website. www.MarcusDolven.example
Should not have
- camera/ lens/ aperture blades

```html
<!DOCTYPE html>
<html lang="en">
<head>
<meta charset="utf-8">
<title>Marcus Dolven Photography — Business Card</title>
<link rel="stylesheet" href="https://fonts.googleapis.com/css2?family=Playfair+Display:wght@400&family=Raleway:wght@300&family=Oswald:wght@300&display=swap">
<style>
  :root {
    --backdrop: #d8d9db;
    --card: #2f353c;
    --card-edge: #262b31;
    --ink: #f2f2f0;
    --ink-soft: #b9bdc2;
    --pattern-base: #30363d;
    --pattern-tone: #4a5058;
  }
  * { box-sizing: border-box; margin: 0; padding: 0; }
  html, body {
    width: 1200px; height: 800px; overflow: hidden;
    background: var(--backdrop);
  }
  .sheet {
    width: 1200px; height: 800px;
    display: flex; align-items: center; justify-content: center; gap: 40px;
  }
  .card {
    width: 560px; height: 320px;
    background: var(--card);
    box-shadow: 0 10px 24px rgba(0,0,0,.18);
    position: relative;
  }
  .card-back {
    background: linear-gradient(135deg, var(--pattern-tone), var(--pattern-base));
  }
  .brand-mark {
    position: absolute; left: 50%; top: 48px;
    width: 86px; height: 86px; margin-left: -43px;
    border-radius: 50%; background: var(--ink);
  }
  .brand-name {
    position: absolute; left: 0; right: 0; top: 150px;
    text-align: center; color: var(--ink);
    font-family: "Playfair Display", serif; font-weight: 400;
    font-size: 32px; letter-spacing: 1px; text-transform: uppercase;
  }
  .brand-trade {
    position: absolute; left: 0; right: 0; top: 196px;
    text-align: center; color: var(--ink-soft);
    font-family: "Raleway", sans-serif; font-weight: 300;
    font-size: 14px; letter-spacing: 7px; text-transform: uppercase;
  }
  .contact-row {
    position: absolute; left: 0; right: 0; bottom: 34px;
    display: flex; justify-content: center; gap: 22px;
    list-style: none;
  }
  .contact-item {
    display: flex; align-items: center; gap: 7px;
    color: var(--ink-soft);
    font-family: "Oswald", sans-serif; font-weight: 300;
    font-size: 11px; letter-spacing: .5px; text-transform: uppercase;
  }
  .contact-icon {
    width: 18px; height: 18px; border-radius: 50%;
    background: var(--ink); color: var(--card);
    display: flex; align-items: center; justify-content: center;
    font-size: 10px; font-weight: 300;
  }
</style>
</head>
<body>
  <main class="sheet">
    <section class="card card-back" role="img" aria-label="Card back: repeating monogram pattern in light grey on charcoal"></section>

    <section class="card card-front">
      <div class="brand-mark" aria-hidden="true"></div>
      <h1 class="brand-name">Marcus Dolven</h1>
      <p class="brand-trade">Photography</p>
      <ul class="contact-row">
        <li class="contact-item"><span class="contact-icon">T</span>306 555 0142</li>
        <li class="contact-item"><span class="contact-icon">E</span>marcusdolven@example.com</li>
        <li class="contact-item"><span class="contact-icon">W</span>www.MarcusDolven.example</li>
      </ul>
    </section>
  </main>
</body>
</html>
```